Veltrano Community Development Planning New web site

Design a new web site. I have a budget of $1,500.00.
Attached on PowerPoint is a complete site plan. Home page and linked pages.
10 - 12 pages. All copy and photos will be supplied. (300dpi)
I have shown them the concept which they like.
No data bases required. Home page with animations dissolving.
They former web site has been taken down. They have been in business 30 years in New Jersey
Colors teal blues and greens
There will be a new logo)being designed)
The text in home page copy will give you a detailed story what they are all about.

files have been approved for Veltrano, Inc.   Tomas is the designer

Industry/Entity Type

Community

```html
<!DOCTYPE html>
<html lang="en">
<head>
<meta charset="utf-8">
<title>Veltrano, Inc</title>
<link href="https://fonts.googleapis.com/css2?family=Play:wght@400;700&display=swap" rel="stylesheet">
<style>
:root{
  --ink:#2b2b2b;
  --muted:#6b6b6b;
  --blue:#0b95d4;
  --blue-dark:#0a7fb5;
  --topbar:#2f3033;
  --footer:#2e3034;
  --soft:#f3f3f3;
  --line:#c9d9e6;
  --white:#ffffff;
}
*{margin:0;padding:0;box-sizing:border-box}
html,body{width:1200px;height:1056px;overflow:hidden}
body{position:relative;background:var(--white);font-family:'Play',sans-serif;color:var(--ink)}
.abs{position:absolute}

/* top utility bar */
.utility{left:273px;top:0;width:650px;height:27px;background:var(--topbar);border-bottom:3px solid var(--blue);color:#9a9a9a;font-size:7px;letter-spacing:.4px;text-transform:uppercase}
.utility .cell{position:absolute;top:0;height:24px;display:flex;align-items:center;gap:10px;padding-left:10px;border-left:1px solid #444;white-space:nowrap;overflow:hidden}
.utility .dot{width:8px;height:8px;background:#bdbdbd;border-radius:2px;flex:none}

/* header */
.logo{left:276px;top:50px;font-size:27px;font-weight:400;color:#111;border-left:3px solid var(--blue);padding-left:3px;line-height:1}
.nav{left:527px;top:44px;display:flex;gap:2px;font-size:10px;color:#222;white-space:nowrap}
.nav a{color:inherit;text-decoration:none;padding:8px 7px;height:26px;display:block}
.nav a.active{background:#ececec;color:var(--blue)}

/* hero */
.hero{left:0;top:89px;width:1200px;height:384px;background:linear-gradient(90deg,#b9c4cf 0%,#8e9eae 30%,#5c6773 55%,#23272d 72%,#3a3f47 85%,#2a2d33 100%)}
.hero-title{left:293px;top:132px;font-size:45px;font-weight:700;color:#fff;white-space:nowrap}
.hero-sub{left:293px;top:186px;font-size:23px;color:#fff;line-height:30px;white-space:nowrap}
.hero-sub b{font-weight:700}
.checks{left:293px;top:250px;list-style:none;color:#f3f3f3;font-size:12px;white-space:nowrap}
.checks li{display:flex;align-items:center;gap:12px;height:36px}
.checks .box{width:20px;height:20px;border:2px solid #fff;display:flex;align-items:center;justify-content:center;flex:none}
.btn{top:364px;height:28px;font-size:12px;color:#fff;display:flex;align-items:center;justify-content:center;white-space:nowrap}
.btn.ghost{left:293px;width:88px;border:2px solid #fff}
.btn.solid{left:392px;width:88px;background:var(--blue)}
.slider-dots{left:573px;top:461px;width:52px;height:22px;background:#fff;border-radius:3px 3px 0 0;display:flex;justify-content:center;align-items:center;gap:5px}
.slider-dots span{width:6px;height:6px;border-radius:50%;background:#c4c4c4}
.slider-dots span.on{background:var(--blue)}

/* intro */
.intro-title{left:0;width:1200px;top:494px;text-align:center;font-size:19px;color:#333}
.intro-title b{font-weight:700}
.intro-text{left:290px;width:620px;top:522px;text-align:center;font-size:11px;line-height:11px;color:#555}

/* about */
.col-title{top:573px;font-size:14px;color:#333;white-space:nowrap}
.col-title b{font-weight:700}
.acc{left:260px;width:327px;border:1px solid var(--line);background:#fff}
.acc .head{height:28px;display:flex;align-items:center;padding:0 10px;gap:10px;color:var(--blue);font-size:12px}
.acc .head .ic{width:16px;height:16px;border-radius:50%;flex:none}
.acc .head svg.chev{margin-left:auto}
.acc .body{padding:6px 8px;font-size:7.5px;line-height:9.5px;color:#777}

/* results */
.results{left:623px;top:610px;width:245px;list-style:none;font-size:9px;line-height:11px;color:#777}
.results li{display:flex;gap:10px;margin-bottom:10px}
.results svg{flex:none}

/* cta band */
.cta{left:0;top:831px;width:1200px;height:90px;background:var(--blue)}
.cta-title{left:281px;top:842px;font-size:21px;color:#fff;white-space:nowrap}
.cta-title b{font-weight:700}
.cta-text{left:281px;top:875px;width:380px;font-size:11px;line-height:13px;color:#fff}
.cta-btn{left:765px;top:858px;width:130px;height:38px;border:1px solid #fff;color:#fff;font-size:17px;display:flex;align-items:center;justify-content:center}

/* memberships */
.members{left:0;top:921px;width:1200px;height:98px;background:var(--soft)}
.members-title{left:0;width:1200px;top:939px;text-align:center;font-size:19px;font-weight:700;color:#333}
.members-list{left:0;width:1200px;top:967px;text-align:center;font-size:12px;line-height:12px;color:#444}

/* footer */
.footer{left:0;top:1019px;width:1200px;height:37px;background:var(--footer)}
.copy{left:260px;top:1032px;font-size:11px;color:#bbb}
.social{left:823px;top:1029px;display:flex;gap:4px}
.social span{width:17px;height:17px;border:1px solid #777;display:flex;align-items:center;justify-content:center}
.social span i{width:6px;height:6px;border-radius:50%;background:#bbb;display:block}
</style>
</head>
<body>

<div class="abs utility">
  <div class="cell" style="left:0;width:82px"><span class="dot"></span>Updates</div>
  <div class="cell" style="left:82px;width:190px"><span class="dot"></span>Community</div>
  <div class="cell" style="left:272px;width:180px">
    <svg width="8" height="8" viewBox="0 0 10 10"><path d="M2 1l2 0 1 2-1 1c.5 1 1.5 2 2.5 2.5l1-1 2 1v2c-4 0-7.5-3.5-7.5-7.5z" fill="#bdbdbd"/></svg>
    Call for support / +1 555 010 2040</div>
  <div class="cell" style="left:452px;width:198px">
    <svg width="8" height="7" viewBox="0 0 10 8"><rect width="10" height="8" fill="#bdbdbd"/><path d="M0 0l5 4 5-4" stroke="#2f3033" fill="none"/></svg>
    Email support / info@veltranoinc.com</div>
</div>

<div class="abs logo">Veltrano, Inc</div>
<nav class="abs nav">
  <a class="active">Home</a><a>Our Company</a><a>Housing Rehab Application</a><a>Affordable Application</a><a>Contact Us</a>
</nav>

<div class="abs hero" role="img" aria-label="Photo of a businessman holding a tablet showing financial charts, blurred city background"></div>
<div class="abs hero-title">Veltrano, Inc</div>
<div class="abs hero-sub">Lorem <b>Ipsum</b> Del<br><b>Gravidar</b> Ipsum <b>dolor</b></div>
<ul class="abs checks">
  <li><span class="box"><svg width="10" height="9" viewBox="0 0 10 9"><path d="M1 5l3 3 5-7" stroke="#fff" stroke-width="2" fill="none"/></svg></span>Proin gravida nibh vel velit auctor aliquet aenean.</li>
  <li><span class="box"><svg width="10" height="9" viewBox="0 0 10 9"><path d="M1 5l3 3 5-7" stroke="#fff" stroke-width="2" fill="none"/></svg></span>Sollicitudin, lorem quis bibendum auctor nisi.</li>
  <li><span class="box"><svg width="10" height="9" viewBox="0 0 10 9"><path d="M1 5l3 3 5-7" stroke="#fff" stroke-width="2" fill="none"/></svg></span>Consequat ipsum, nec sagittis sem nibh.</li>
</ul>
<div class="abs btn ghost">Our Company</div>
<div class="abs btn solid">Contact Us</div>
<div class="abs slider-dots"><span class="on"></span><span></span><span></span></div>

<h1 class="abs intro-title" style="font-weight:400">Want to know about <b>Veltrano, Inc</b></h1>
<p class="abs intro-text">Community Development Planning * Housing Rehabilitation Administration * National Housing Renewal Office (NHRO) Program Management * Implementation of Programs under the Jurisdiction of State Council of Affordable Housing (SCAH)</p>

<h2 class="abs col-title" style="left:260px;font-weight:400">About <b>Veltrano, Inc</b></h2>
<div class="abs acc" style="top:612px">
  <div class="head"><span class="ic" style="background:#e7a23a"></span>Who we are?<svg class="chev" width="12" height="7" viewBox="0 0 12 7"><path d="M1 1l5 5 5-5" stroke="#0b95d4" fill="none" stroke-width="1.5"/></svg></div>
</div>
<div class="abs acc" style="top:648px">
  <div class="head"><span class="ic" style="background:#a0524a"></span>Our Mission<svg class="chev" width="12" height="7" viewBox="0 0 12 7"><path d="M1 1l5 5 5-5" stroke="#0b95d4" fill="none" stroke-width="1.5"/></svg></div>
</div>
<div class="abs acc" style="top:685px">
  <div class="head"><span class="ic" style="border:1.5px solid #0b95d4;font-size:10px;display:flex;align-items:center;justify-content:center">?</span>How do we do it?<svg class="chev" width="12" height="7" viewBox="0 0 12 7"><path d="M1 1l5 5 5-5" stroke="#0b95d4" fill="none" stroke-width="1.5"/></svg></div>
</div>
<div class="abs acc" style="top:721px;height:91px">
  <div class="head"><span class="ic" style="border-radius:2px;width:12px;background:#1d6fa8"></span>Essential Facts<svg class="chev" width="7" height="12" viewBox="0 0 7 12"><path d="M1 1l5 5-5 5" stroke="#0b95d4" fill="none" stroke-width="1.5"/></svg></div>
  <div class="body">Lorem ipsum dolor sit amet, consectetur adipisicing elit, sed do eiusmod tempor incididunt ut labore et dolore magna aliqua. Ut enim ad minim veniam, quis nostrud exercitation ullamco laboris nisi ut aliquip ex ea commodo consequat. Duis aute irure dolor in reprehenderit in voluptate velit esse cillum dolore eu fugiat nulla pariatur. Excepteur sint occaecat cupidatat non proident, sunt in culpa qui officia deserunt mollit anim id.</div>
</div>

<h2 class="abs col-title" style="left:617px;top:574px;font-weight:400">We Get <b>Results</b></h2>
<ul class="abs results">
  <li><svg width="12" height="12" viewBox="0 0 12 12"><rect x=".5" y="1.5" width="10" height="10" fill="none" stroke="#0b95d4"/><path d="M2.5 6l2.5 3 6-8" stroke="#0b95d4" stroke-width="2" fill="none"/></svg><span>Veltrano designs income based programs to be supported by federal placement lotteries state funding</span></li>
  <li><svg width="12" height="12" viewBox="0 0 12 12"><rect x=".5" y="1.5" width="10" height="10" fill="none" stroke="#0b95d4"/><path d="M2.5 6l2.5 3 6-8" stroke="#0b95d4" stroke-width="2" fill="none"/></svg><span>We implement local programs to benefit people seeking access to affordable housing</span></li>
  <li><svg width="12" height="12" viewBox="0 0 12 12"><rect x=".5" y="1.5" width="10" height="10" fill="none" stroke="#0b95d4"/><path d="M2.5 6l2.5 3 6-8" stroke="#0b95d4" stroke-width="2" fill="none"/></svg><span>Our experienced staff screen applicants for local affordable housing</span></li>
  <li><svg width="12" height="12" viewBox="0 0 12 12"><rect x=".5" y="1.5" width="10" height="10" fill="none" stroke="#0b95d4"/><path d="M2.5 6l2.5 3 6-8" stroke="#0b95d4" stroke-width="2" fill="none"/></svg><span>We pre-qualify persons who have applied for housing rehabilitation</span></li>
  <li><svg width="12" height="12" viewBox="0 0 12 12"><rect x=".5" y="1.5" width="10" height="10" fill="none" stroke="#0b95d4"/><path d="M2.5 6l2.5 3 6-8" stroke="#0b95d4" stroke-width="2" fill="none"/></svg><span>Conduct placement lotteries</span></li>
  <li><svg width="12" height="12" viewBox="0 0 12 12"><rect x=".5" y="1.5" width="10" height="10" fill="none" stroke="#0b95d4"/><path d="M2.5 6l2.5 3 6-8" stroke="#0b95d4" stroke-width="2" fill="none"/></svg><span>Through local housing rehabilitation programs, our experience construction inspectors determine what improvements are required at eligible units based on local building codes and health and safety issues</span></li>
</ul>

<div class="abs cta"></div>
<div class="abs cta-title">Do you need <b>more information?</b></div>
<p class="abs cta-text">This is Layoutcraft's version of Lorem Ipsum. Proin gravida nibh vel velit auctor aliquet. Aenean sollicitudin, lorem quis bibendum auctor.</p>
<div class="abs cta-btn">Contact Us</div>

<div class="abs members"></div>
<div class="abs members-title">Memberships</div>
<p class="abs members-list">National Neighborhood Renewal Council &nbsp; Garden State Planning Guild<br>Regional Planning Officials Forum &nbsp;Garden State Housing Alliance</p>

<div class="abs footer"></div>
<div class="abs copy">© Copyright Veltrano,Inc 2014. All Rights Reserved.</div>
<div class="abs social"><span><i></i></span><span><i></i></span><span><i></i></span><span><i></i></span><span><i></i></span></div>

</body>
</html>
```